The Pemberly Nine Modes of Inventive Spark Graphics

DESIGN ELEMENT 1: The Pemberly Nine Modes of Inventive Spark Wheel/Circle
A circular diagram showing all 12 types organized by their three domains.
I attached what I have so far, I created this in PPT. It uses some of the elements you have already created for me like the colors and fonts.
I've also attached a representation of the 3 Domains (Relational, Analytical and Functional)
DESIGN ELEMENT 2: The Nine Personas of Inventive Spark (Human Representations)
The Connector, The Cultivator, The Healer, The Teacher, The Communicator, The Scientist, The Strategist, The Synthesizer, The Artist, The Builder, The Designer, The Organizer.
Each of the 12 types represented as a human figure.
Style options to consider:
• Silhouettes — Clean, simple, universal (gender-neutral, racially ambiguous). Each silhouette could hold or interact with a symbol of their type.
• Or Illustrated figures — More personality, could show action/posture that reflects the type (e.g., Connector introducing people reaching out hands, Builder holding tools, Artist painting, Strategist looking toward horizon)
• Abstract/geometric figures — Modern, stylized human forms with symbolic elements
Key considerations:
• Diversity & inclusivity — If using detailed illustrations, represent diverse ages, genders, races, body types. If using silhouettes, keep them universal.
• Action/posture — Each figure should be doing something that reflects their type (connecting, building, healing, teaching, etc.)
• Consistency — All 12 should feel like they belong to the same visual family while being distinct from each other.
An idea: Silhouettes might be strongest—they're inclusive, timeless, and let the reader project themselves into the type. Each silhouette could be shown with one signature object or in one signature pose. But I’m open to other ideas.
TONE & FEEL
• Empowering — "You ARE creative"
• Inclusive — For corporations, classrooms, faith congregations, clinics, communities
• Warm but credible — Grounded in psychology research, but accessible and human
• Revolutionary — "The Inventive Spark Uprising"
The design should feel:
• Modern but not cold
• Professional but not too corporate
• Hopeful, energizing, inviting
• Sophisticated enough for business readers, warm enough for everyone else

```html
<!DOCTYPE html>
<html lang="en">
<head>
<meta charset="utf-8">
<title>The Pemberly Nine Modes of Inventive Spark</title>
<link href="https://fonts.googleapis.com/css2?family=Open+Sans:wght@400;600;700&family=Lato:wght@400&display=swap" rel="stylesheet">
<style>
  :root {
    --designer: #a3a3dd;
    --organizer: #6b2f87;
    --connector: #b52d7e;
    --cultivator: #f47fb4;
    --healer: #ec2a7b;
    --teacher: #7e1539;
    --synthesizer: #dd1f26;
    --strategist: #ef5a50;
    --scientist: #f39322;
    --communicator: #f8bf7d;
    --artist: #35378c;
    --builder: #7777cb;
    --ink: #1a1a1a;
    --paper: #ffffff;
    --label: #ffffff;
  }
  * { margin: 0; padding: 0; box-sizing: border-box; }
  html, body {
    width: 960px;
    height: 1200px;
    overflow: hidden;
    background: var(--paper);
  }
  .poster {
    position: relative;
    width: 960px;
    height: 1200px;
  }
  .wheel {
    position: absolute;
    left: 0;
    top: 0;
    width: 960px;
    height: 960px;
  }
  .segment { stroke: var(--paper); stroke-width: 4; }
  .seg-designer { fill: var(--designer); }
  .seg-organizer { fill: var(--organizer); }
  .seg-connector { fill: var(--connector); }
  .seg-cultivator { fill: var(--cultivator); }
  .seg-healer { fill: var(--healer); }
  .seg-teacher { fill: var(--teacher); }
  .seg-synthesizer { fill: var(--synthesizer); }
  .seg-strategist { fill: var(--strategist); }
  .seg-scientist { fill: var(--scientist); }
  .seg-communicator { fill: var(--communicator); }
  .seg-artist { fill: var(--artist); }
  .seg-builder { fill: var(--builder); }
  .type-label {
    font-family: "Open Sans", Arial, sans-serif;
    font-weight: 700;
    font-size: 17px;
    fill: var(--label);
    text-anchor: middle;
    dominant-baseline: middle;
  }
  .type-label.light { font-weight: 400; }
  .title {
    position: absolute;
    left: 253px;
    top: 410px;
    width: 452px;
    text-align: center;
  }
  .title-lead {
    font-family: "Lato", Arial, sans-serif;
    font-size: 25px;
    color: var(--ink);
    letter-spacing: -0.2px;
    line-height: 1.2;
  }
  .title-name {
    font-family: "Open Sans", Arial, sans-serif;
    font-weight: 600;
    font-size: 40px;
    color: var(--connector);
    line-height: 1.3;
  }
  .lineup {
    position: absolute;
    left: 60px;
    top: 950px;
    width: 856px;
    height: 160px;
    border-radius: 8px;
    background: linear-gradient(90deg,
      var(--connector), var(--cultivator), var(--artist), var(--scientist),
      var(--strategist), var(--builder), var(--organizer), var(--communicator));
    opacity: 0.85;
  }
  .ground {
    position: absolute;
    left: 38px;
    top: 1108px;
    width: 884px;
    height: 6px;
    border-radius: 50%;
    background: var(--ink);
  }
</style>
</head>
<body>
<main class="poster">
  <svg class="wheel" viewBox="0 0 960 960" aria-label="Wheel of twelve creative types">
    <g class="segments">
      <path class="segment seg-designer" role="img" aria-label="Designer silhouette holding a laptop and stylus, with a drafting compass" d="M479 72 A407 407 0 0 1 682.5 126.5 L592 283.3 A226 226 0 0 0 479 253 Z"/>
      <path class="segment seg-organizer" role="img" aria-label="Organizer silhouette holding a square, circle and triangle" d="M682.5 126.5 A407 407 0 0 1 831.5 275.5 L674.7 366 A226 226 0 0 0 592 283.3 Z"/>
      <path class="segment seg-connector" role="img" aria-label="Connector silhouette with arms stretched wide" d="M831.5 275.5 A407 407 0 0 1 886 479 L705 479 A226 226 0 0 0 674.7 366 Z"/>
      <path class="segment seg-cultivator" role="img" aria-label="Cultivator silhouette kneeling and holding a seedling" d="M886 479 A407 407 0 0 1 831.5 682.5 L674.7 592 A226 226 0 0 0 705 479 Z"/>
      <path class="segment seg-healer" role="img" aria-label="Healer silhouette with hands cupped around a heart" d="M831.5 682.5 A407 407 0 0 1 682.5 831.5 L592 674.7 A226 226 0 0 0 674.7 592 Z"/>
      <path class="segment seg-teacher" role="img" aria-label="Teacher silhouette holding a book and pointing to a lightbulb" d="M682.5 831.5 A407 407 0 0 1 479 886 L479 705 A226 226 0 0 0 592 674.7 Z"/>
      <path class="segment seg-synthesizer" role="img" aria-label="Synthesizer silhouette balancing two shapes in open hands" d="M479 886 A407 407 0 0 1 275.5 831.5 L366 674.7 A226 226 0 0 0 479 705 Z"/>
      <path class="segment seg-strategist" role="img" aria-label="Strategist silhouette pointing ahead toward a chess knight" d="M275.5 831.5 A407 407 0 0 1 126.5 682.5 L283.3 592 A226 226 0 0 0 366 674.7 Z"/>
      <path class="segment seg-scientist" role="img" aria-label="Scientist silhouette holding an atom symbol" d="M126.5 682.5 A407 407 0 0 1 72 479 L253 479 A226 226 0 0 0 283.3 592 Z"/>
      <path class="segment seg-communicator" role="img" aria-label="Communicator silhouette speaking into a microphone with a speech bubble" d="M72 479 A407 407 0 0 1 126.5 275.5 L283.3 366 A226 226 0 0 0 253 479 Z"/>
      <path class="segment seg-artist" role="img" aria-label="Artist silhouette holding a paintbrush and palette" d="M126.5 275.5 A407 407 0 0 1 275.5 126.5 L366 283.3 A226 226 0 0 0 283.3 366 Z"/>
      <path class="segment seg-builder" role="img" aria-label="Builder silhouette holding a wrench" d="M275.5 126.5 A407 407 0 0 1 479 72 L479 253 A226 226 0 0 0 366 283.3 Z"/>
    </g>
    <g class="labels">
      <text class="type-label" x="563" y="175">The Designer</text>
      <text class="type-label" x="713" y="245">The Organizer</text>
      <text class="type-label" x="789" y="402">The Connector</text>
      <text class="type-label" x="787" y="556">The Cultivator</text>
      <text class="type-label" x="713" y="711">The Healer</text>
      <text class="type-label" x="563" y="797">The Teacher</text>
      <text class="type-label" x="392" y="795">The Synthesizer</text>
      <text class="type-label light" x="246" y="711">The Strategist</text>
      <text class="type-label" x="175" y="556">The Scientist</text>
      <text class="type-label" x="176" y="402">The Communicator</text>
      <text class="type-label" x="247" y="246">The Artist</text>
      <text class="type-label" x="398" y="177">The Builder</text>
    </g>
  </svg>

  <h1 class="title">
    <span class="title-lead">The Pemberly Nine Modes of</span><br>
    <span class="title-name">Inventive Spark</span>
  </h1>

  <div class="lineup" role="img" aria-label="A row of twelve coloured silhouettes, one for each creative type, each with its signature object"></div>
  <div class="ground"></div>
</main>
</body>
</html>
```